Jewelry Shop Needs a Business Card Design

***We want a very sharp and unforgettable pantone for the Business Card. ***
***We do not want the business card or logo only in black, white and grey color!!!Please provide us a main color as our brand topic! Thanks!! ***

Mabel’s Nook is a Hong Kong based fine jewelry brand.

We want a very nice, simple and elegant business card design for Mabel's Nook Brand. The company's logo has been uploaded already.

You can design with below info:

Desmond Yip
Director
M: +852 94726305
T: +852 35842947
F: +852 35842949
E: desmond.yip@mabelsnook.example
9/F , Harbourlight Tower, 18-24 Fenwick Lane, Sai Wan Ho, Kowloon, Hong Kong

Target Market(s)

Mabel’s Nook philosophy is a jewelry icon of young, creative, trendy, fashionable, stylish, energetic, and elegant. For Mabel’s Nook, jewelry is one collection of artworks, the most important items in personal life.

Industry/Entity Type

Jewelry

Requirements
Must have
• We want a very sharp and unforgettable pantone for the Business Card.

```html
<!DOCTYPE html>
<html lang="en">
<head>
<meta charset="utf-8">
<title>Mabel’s Nook — Business Card</title>
<link rel="stylesheet" href="https://fonts.googleapis.com/css2?family=Cinzel:wght@400;500&display=swap">
<style>
  :root {
    --backdrop: #ecebe8;
    --card: #ffffff;
    --card-edge: #dcdcdc;
    --brand: #9e1b4f;        /* jewel ruby-magenta brand colour */
    --brand-faint: #f7e9ef;
    --ink: #3b3838;
    --ink-soft: #9e1b4f;
  }
  * { box-sizing: border-box; margin: 0; padding: 0; }
  html, body {
    width: 1200px; height: 913px; overflow: hidden;
    background: var(--backdrop);
    font-family: "Cinzel", "Trajan Pro", serif;
    color: var(--ink);
  }
  .canvas { position: relative; width: 1200px; height: 913px; }
  .card {
    position: absolute;
    width: 540px; height: 310px;
    background: var(--card);
    border: 1px solid var(--card-edge);
    box-shadow: 0 6px 18px rgba(0,0,0,0.12);
    overflow: hidden;
  }
  .card--front { left: 90px; top: 110px; }
  .card--back { left: 580px; top: 500px; }

  .decor-circle {
    position: absolute;
    width: 300px; height: 300px; border-radius: 50%;
    background: var(--brand-faint);
    right: -90px; top: -110px;
  }
  .brand-dot {
    position: absolute;
    border-radius: 50%;
    background: var(--brand);
  }
  .card--front .brand-dot { width: 110px; height: 110px; left: 215px; top: 62px; }
  .card--back .brand-dot { width: 84px; height: 84px; left: 78px; top: 92px; }

  .brand-name {
    position: absolute;
    font-weight: 500;
    letter-spacing: 0.08em;
    color: var(--brand);
    white-space: nowrap;
  }
  .card--front .brand-name { font-size: 30px; left: 0; right: 0; top: 196px; text-align: center; }
  .card--back .brand-name { font-size: 17px; left: 40px; width: 160px; text-align: center; top: 188px; }

  .contact {
    position: absolute; left: 270px; top: 58px;
    font-size: 11.5px; line-height: 1.45; letter-spacing: 0.03em;
    white-space: nowrap;
  }
  .contact__name { font-size: 15px; letter-spacing: 0.06em; color: var(--brand); }
  .contact__role { font-size: 9px; color: var(--ink-soft); letter-spacing: 0.08em; margin-bottom: 18px; }
  .contact__lines { list-style: none; margin-bottom: 18px; }
  .contact__address { font-style: normal; }
</style>
</head>
<body>
<main class="canvas">
  <section class="card card--front" aria-label="Card front">
    <div class="decor-circle" aria-hidden="true"></div>
    <div class="brand-dot" aria-hidden="true"></div>
    <p class="brand-name">Mabel’s Nook</p>
  </section>

  <section class="card card--back" aria-label="Card back">
    <div class="brand-dot" aria-hidden="true"></div>
    <p class="brand-name">Mabel’s Nook</p>
    <div class="contact">
      <p class="contact__name">Desmond Yip</p>
      <p class="contact__role">Director</p>
      <ul class="contact__lines">
        <li>M: +852 94726305</li>
        <li>T: +852 35842947</li>
        <li>F: +852 35842949</li>
        <li>E: desmond.yip@mabelsnook.example</li>
      </ul>
      <address class="contact__address">
        9/F , Harbourlight Tower,<br>
        18-24 Fenwick Lane, Sai Wan Ho,<br>
        Kowloon, Hong Kong
      </address>
    </div>
  </section>
</main>
</body>
</html>
```